Looking for potential sellers

We help people buy and sell homes and are currently looking for potential home sellers. We offer low commissions, are the Local Harborview Experts, homes selling fast and at top dollar, Free expert pricing opinions and Consultations, over 9 years of experience, top rated Realtors creative and aggressive marketing strategies. Never merely own a house, THRIVE at Harborview. phone number 482-630-9157 web thriveatharborview.com

```html
<!DOCTYPE html>
<html lang="en">
<head>
<meta charset="utf-8">
<title>Lakemont Realty Company – Thrive at Harborview</title>
<link href="https://fonts.googleapis.com/css2?family=Montserrat:wght@300;400;500;600;700&display=swap" rel="stylesheet">
<style>
  :root {
    --olive: #9a9935;
    --white: #ffffff;
    --ink: #231f20;
    --photo-light: #e6e7ea;
    --photo-mid: #b9a59a;
    --photo-dark: #3e4a63;
  }
  * { margin: 0; padding: 0; box-sizing: border-box; }
  html, body {
    width: 1200px;
    height: 811px;
    overflow: hidden;
    background: var(--white);
  }
  .ad {
    position: relative;
    width: 1200px;
    height: 811px;
    font-family: "Montserrat", sans-serif;
    display: grid;
    grid-template-columns: 581px 619px;
  }
  .agent-photo {
    grid-row: 1 / span 2;
    height: 811px;
    background:
      radial-gradient(ellipse 55% 45% at 40% 30%, var(--photo-mid) 0%, rgba(185,165,154,0) 70%),
      linear-gradient(180deg, var(--photo-light) 0%, #d9dadd 45%, var(--photo-dark) 100%);
  }
  .brand-panel {
    height: 324px;
    background: var(--white);
    display: flex;
    align-items: center;
    justify-content: center;
  }
  .brand {
    display: flex;
    align-items: center;
    gap: 18px;
    color: var(--ink);
  }
  .brand-mark {
    width: 26px;
    height: 26px;
    background: var(--olive);
  }
  .brand-name {
    font-size: 40px;
    font-weight: 500;
    letter-spacing: 0.5px;
    line-height: 1.15;
  }
  .message-panel {
    height: 487px;
    background: var(--olive);
    color: var(--white);
    padding: 98px 40px 0 43px;
    position: relative;
  }
  .tagline {
    font-size: 37px;
    line-height: 1.3;
  }
  .tagline-lead {
    display: block;
    font-weight: 300;
  }
  .tagline-accent {
    display: block;
    font-weight: 700;
  }
  .seller-points {
    position: absolute;
    left: 43px;
    top: 232px;
    list-style: none;
    font-size: 21px;
    font-weight: 400;
    line-height: 1.45;
  }
  .seller-points li {
    display: flex;
    align-items: center;
    gap: 12px;
  }
  .seller-points li::before {
    content: "";
    width: 8px;
    height: 8px;
    background: var(--white);
    flex: none;
  }
  .seller-points strong { font-weight: 700; }
  .contact {
    position: absolute;
    left: 43px;
    top: 382px;
    font-size: 27px;
    font-weight: 500;
    line-height: 1.22;
    list-style: none;
  }
</style>
</head>
<body>
  <main class="ad">
    <div class="agent-photo" role="img" aria-label="Portrait photo of a smiling real estate agent with red hair and beard, wearing a plaid shirt, against a light grey backdrop"></div>

    <header class="brand-panel">
      <div class="brand">
        <span class="brand-mark" aria-hidden="true"></span>
        <span class="brand-name">Lakemont Realty<br>Company</span>
      </div>
    </header>

    <section class="message-panel">
      <h1 class="tagline">
        <span class="tagline-lead">Never merely own a house,</span>
        <span class="tagline-accent">THRIVE at Harborview.</span>
      </h1>
      <ul class="seller-points">
        <li><span><strong>Selling?</strong> Low commissions</span></li>
        <li>Free expert pricing opinions</li>
        <li>Local experts, 9+ years, fast sales</li>
      </ul>
      <ul class="contact">
        <li class="contact-phone">482-630-9157</li>
        <li class="contact-web">thriveatharborview.com</li>
      </ul>
    </section>
  </main>
</body>
</html>
```